Upscale business cards needed for Board of Directors

We need professional business cards created for members of our family business Board of Directors. We would like these relatively simple and straightforward, but also with a unique element to set them apart. Probably stick with neutral and simple colors - white, grey etc. We need space for the traditional elements, including name, title, address, email/phone number. And we will be creating several from this template so it needs to be template that is easy to switch information in and out of.
Business
See description

```html
<!DOCTYPE html>
<html lang="en">
<head>
<meta charset="utf-8">
<title>Harborline Holdings – Business Card</title>
<link href="https://fonts.googleapis.com/css2?family=Lato:wght@400;700&display=swap" rel="stylesheet">
<style>
  :root {
    --bg: #3a3a3a;
    --card-black: #050505;
    --card-white: #ffffff;
    --ink: #111111;
    --gold: #b39c72;
    --muted-white: #e8e8e8;
  }
  * { margin: 0; padding: 0; box-sizing: border-box; }
  html, body { width: 1200px; height: 900px; overflow: hidden; }
  body {
    background: var(--bg);
    font-family: "Lato", sans-serif;
    position: relative;
  }
  .card {
    position: absolute;
    left: 250px;
    width: 700px;
    height: 400px;
    box-shadow: 0 10px 30px rgba(0,0,0,0.45);
  }
  .card--back {
    top: 40px;
    background: var(--card-black);
    display: flex;
    flex-direction: column;
    align-items: center;
    justify-content: center;
  }
  .card--front {
    top: 460px;
    background: var(--card-white);
  }
  .brand {
    display: inline-block;
  }
  .brand__rule {
    height: 5px;
    background: var(--gold);
    margin-bottom: 14px;
  }
  .brand__name {
    font-weight: 700;
    font-size: 42px;
    line-height: 1;
    white-space: nowrap;
  }
  .card--back .brand__name { color: var(--card-white); }
  .card--back .web {
    margin-top: 48px;
    color: var(--muted-white);
    font-size: 17px;
    letter-spacing: 2px;
  }
  .card--front .brand {
    position: absolute;
    left: 44px;
    top: 50px;
  }
  .card--front .brand__name { color: var(--ink); font-size: 38px; }
  .contact {
    position: absolute;
    left: 44px;
    top: 170px;
    color: var(--ink);
    font-size: 18px;
    line-height: 1.25;
  }
  .contact__address { margin-bottom: 10px; padding-left: 32px; }
  .contact__row { display: flex; align-items: center; gap: 14px; height: 25px; }
  .contact__row svg { width: 18px; height: 18px; flex: none; fill: var(--gold); }
  .person {
    position: absolute;
    left: 430px;
    top: 280px;
  }
  .person__name { color: var(--gold); font-size: 30px; font-weight: 400; }
  .person__title { color: var(--ink); font-size: 20px; margin-top: 2px; }
</style>
</head>
<body>
  <section class="card card--back">
    <div class="brand">
      <div class="brand__rule"></div>
      <p class="brand__name">Harborline Holdings</p>
    </div>
    <p class="web">www.harborline.com</p>
  </section>

  <section class="card card--front">
    <div class="brand">
      <div class="brand__rule"></div>
      <p class="brand__name">Harborline Holdings</p>
    </div>

    <div class="contact">
      <p class="contact__address">4100 Cedar Lane<br>Lakeview TX 78000</p>
      <p class="contact__row">
        <svg viewBox="0 0 24 24" aria-hidden="true"><path d="M6.6 10.8a15.2 15.2 0 0 0 6.6 6.6l2.2-2.2c.3-.3.7-.4 1-.2 1.1.4 2.3.6 3.6.6.6 0 1 .4 1 1V20c0 .6-.4 1-1 1A17 17 0 0 1 3 4c0-.6.4-1 1-1h3.5c.6 0 1 .4 1 1 0 1.3.2 2.5.6 3.6.1.3 0 .7-.2 1z"/></svg>
        512 004 2200
      </p>
      <p class="contact__row">
        <svg viewBox="0 0 24 24" aria-hidden="true"><path d="M6 3h12v5H6zM4 9h16a2 2 0 0 1 2 2v6h-4v4H6v-4H2v-6a2 2 0 0 1 2-2zm4 6v4h8v-4z"/></svg>
        512 004 2201
      </p>
      <p class="contact__row">
        <svg viewBox="0 0 24 24" aria-hidden="true"><path d="M2 5h20v14H2zm2 2v.5l8 5 8-5V7z"/></svg>
        info@harborline.com
      </p>
      <p class="contact__row">
        <svg viewBox="0 0 24 24" aria-hidden="true"><path d="M12 2a10 10 0 1 0 0 20 10 10 0 0 0 0-20zm6.9 6h-3a15 15 0 0 0-1.3-3.9A8 8 0 0 1 18.9 8zM12 4c.8 1.2 1.5 2.5 1.9 4h-3.8c.4-1.5 1.1-2.8 1.9-4zM4.3 14a8 8 0 0 1 0-4h3.4a16 16 0 0 0 0 4zm.8 2h3a15 15 0 0 0 1.3 3.9A8 8 0 0 1 5.1 16zm3-8h-3a8 8 0 0 1 4.3-3.9C8.8 5.3 8.4 6.6 8.1 8zM12 20c-.8-1.2-1.5-2.5-1.9-4h3.8c-.4 1.5-1.1 2.8-1.9 4zm2.3-6H9.7a14 14 0 0 1 0-4h4.6a14 14 0 0 1 0 4zm.3 5.9c.6-1.2 1-2.5 1.3-3.9h3a8 8 0 0 1-4.3 3.9zm1.7-5.9a16 16 0 0 0 0-4h3.4a8 8 0 0 1 0 4z"/></svg>
        www.harborline.com
      </p>
    </div>

    <div class="person">
      <p class="person__name">Daniel Marsh</p>
      <p class="person__title">Director</p>
    </div>
  </section>
</body>
</html>
```